International Trade Consulting Firm Seeks Quality Newsletter Design

Our company provides consulting services to Meridian 700 type companies. We compete with the largest consulting companies in the world. However, we have the highest level of expertise in the industry and need to look the most professional and high end. We have very relevant and important information to provide our customers about their compliance and projects. We will have the winning design coded to be an e-newsletter, so it needs to be one page. We want to keep our company colors and logo design in the newsletter, they are attached. We DO NOT want it to look like a mini-version of our website. We want a fresh look to this marketing piece. Newsletter will need to include title, possible sub-heading, space for a feature story, 2 other stories included, and space on either the left or right for short cuts, links or highlights of other articles. Contents/'In this issue' section, about us or branding area, section for relevant links, etc...
Target Market(s)
Meridian 700 companies, High-level management
Industry/Entity Type
Marketing

```html
<!DOCTYPE html>
<html lang="en">
<head>
<meta charset="utf-8">
<title>Newsletter</title>
<link rel="stylesheet" href="https://fonts.googleapis.com/css2?family=Arimo:wght@400;700&family=Questrial&display=swap">
<style>
:root{
  --page:#ececec;
  --header:#d5d9de;
  --sidebar:#d7dbe2;
  --panel:#e7e9ee;
  --rule:#ffffff;
  --band-top:#e3e6eb;
  --band-bottom:#a8b0be;
  --band-dark-top:#b6bdc9;
  --band-dark-bottom:#7f8aa0;
  --title:#2f3f5a;
  --text:#5c6170;
  --muted:#7d8290;
  --ink:#111111;
  --placeholder:#9fb8cf;
}
*{box-sizing:border-box;margin:0;padding:0}
html,body{width:1200px;height:1000px;overflow:hidden;background:var(--page)}
body{font-family:"Arimo",Arial,sans-serif;color:var(--text);position:relative}
.newsletter{position:absolute;left:331px;top:0;width:627px;height:1000px;background:var(--rule)}
.masthead{position:absolute;left:0;top:0;width:627px;height:68px;background:var(--header)}
.brand{position:absolute;left:8px;top:24px;display:flex;align-items:center;gap:8px;font-weight:700;font-size:13px;color:var(--title)}
.brand-mark{width:13px;height:13px;background:var(--title)}
.masthead h1{position:absolute;left:277px;top:6px;font-weight:400;font-size:24px;color:var(--ink)}
.masthead h2{position:absolute;left:205px;top:35px;font-weight:400;font-size:16px;color:var(--ink)}
.sidebar{position:absolute;left:2px;top:70px;width:210px;height:850px;background:var(--sidebar)}
.main{position:absolute;left:215px;top:70px;width:407px;height:850px;background:var(--panel)}
.band{height:34px;background:linear-gradient(var(--band-top),var(--band-bottom));display:flex;align-items:center;justify-content:space-between;padding:0 18px;font-family:"Questrial",sans-serif;font-size:14.5px;letter-spacing:.5px;color:var(--title);border-bottom:1px solid #9aa2b0}
.band.dark{background:linear-gradient(var(--band-dark-top),var(--band-dark-bottom));color:#fff}
.issue-list{list-style:none}
.issue-list li{height:25px;line-height:26px;padding-left:22px;font-size:10px;letter-spacing:.3px;border-bottom:1px solid #fff;position:relative}
.issue-list li::before{content:"";position:absolute;left:12px;top:12px;width:4px;height:1px;background:var(--muted)}
.news-item{padding:14px 16px 0;border-bottom:2px solid #fff;font-size:10px;line-height:12.5px;letter-spacing:.35px}
.news-item h4{font-size:9.5px;font-weight:700;margin-bottom:6px;line-height:10.5px}
.news-item.first{height:82px}
.news-item.second{height:101px}
.gap{height:3px;background:#fff}
.footnote{padding:19px 16px;font-size:9.5px;line-height:13px;letter-spacing:.3px;color:var(--muted)}
.footnote b{color:var(--text)}
.story{padding:15px 26px 0 22px;font-size:10px;line-height:13.5px;letter-spacing:.4px}
.story p+p{margin-top:7px}
.story.intro{height:100px}
.story.feature{height:255px}
.photo{float:left;width:168px;height:114px;margin:0 22px 6px 0;border:3px solid #fff;background:var(--placeholder)}
.bullets{height:88px;padding:17px 22px 0 34px;font-size:10.5px;line-height:15px;letter-spacing:.35px}
.bullets li{margin-bottom:8px;color:var(--text)}
.bullets li::marker{color:#a0a6b2;font-size:9px}
.divider{height:2px;background:#fff}
.site-footer{position:absolute;left:2px;top:923px;width:620px;height:74px;background:var(--panel);border:1px solid #b7bdc8;text-align:center;font-size:7.5px;font-weight:700;line-height:9.5px;letter-spacing:.3px;color:var(--text);padding-top:23px}
.site-footer a{color:var(--title)}
</style>
</head>
<body>
<div class="newsletter">
  <header class="masthead">
    <div class="brand"><span class="brand-mark"></span>Harborline Trade Group</div>
    <h1>Heading</h1>
    <h2>Sub-heading</h2>
  </header>

  <aside class="sidebar">
    <div class="band">In This Issue
      <svg width="24" height="12" viewBox="0 0 24 12"><rect x="0.5" y="0.5" width="23" height="11" fill="#f3f4f6" stroke="#9aa2b0"/><path d="M0.5 0.5 L12 7 L23.5 0.5" fill="none" stroke="#9aa2b0"/></svg>
    </div>
    <ul class="issue-list">
      <li>Lorem ipsum dolor amet</li>
      <li>Donce imperiat accumsan felis</li>
      <li>Aliquam lectus orci, adipiscing</li>
    </ul>
    <div class="band">Other News
      <svg width="26" height="16" viewBox="0 0 26 16"><path d="M1 15 L13 1 L25 15 Z" fill="#f3f4f6" stroke="#9aa2b0"/></svg>
    </div>
    <div class="news-item first"><h4>Iriure hendrerit insitam quod</h4>Et quinta decima eodem modo typi qui nunc nobis videntur parum clari fiant sollemnes in.</div>
    <div class="news-item second"><h4>Iusto odio dignissim quindit praesent luptatum zzril.</h4>Nonummy nibh euismod tincidunt ut laoreet dolore magna aliquam erat! Hendrerit in.</div>
    <div class="band dark">Forward Email
      <svg width="28" height="12" viewBox="0 0 28 12"><rect x="4.5" y="0.5" width="23" height="11" fill="#eef0f3" stroke="#7f8aa0"/><path d="M0 6 H14 M10 3 L14 6 L10 9" fill="none" stroke="#2f3f5a" stroke-width="2"/></svg>
    </div>
    <div class="gap"></div>
    <div class="band dark">Unsubscribe
      <svg width="28" height="12" viewBox="0 0 28 12"><rect x="4.5" y="0.5" width="23" height="11" fill="#eef0f3" stroke="#7f8aa0"/><path d="M2 2 L9 10 M9 2 L2 10" stroke="#2f3f5a" stroke-width="2"/></svg>
    </div>
    <p class="footnote">You're receiving this newsletter because you signed up at <b>yoursite.com / bought widgets from us.</b><br>Having trouble reading this email? <b>View it in your browser.</b></p>
  </aside>

  <main class="main">
    <div class="band">Me lius quod ii legunt saepius claritas</div>
    <div class="story intro"><p>Quis nostrud exerci tation ullamcorper suscipit lobortis nisl ut aliquip ex ea commodo consequat. Ipsum dolor sit amet consectetuer adipiscing elit sed diam nonummy nibh euismod tincidunt. Demonstraverunt lectores legere me lius quod ii legunt saepius claritas est etiam processus dynamicus qui sequitur.</p></div>
    <div class="divider"></div>
    <div class="band">Ut laoreet dolore magna, aliquam erat</div>
    <div class="story feature">
      <div class="photo" role="img" aria-label="Feature story photograph"></div>
      <p>Quis nostrud exerci tation ullamcorper suscipit lobortis nisl ut aliquip ex ea commodo consequat. Ipsum dolor sit amet consectetuer adipiscing elit sed diam nonummy nibh euismod tincidunt. Demonstraverunt lectores legere me lius quod ii legunt saepius claritas est etiam processus dynamicus qui sequitur. Quis nostrud exerci tation ullamcorper suscipit lobortis nisl ut aliquip ex ea commodo consequat. Ipsum dolor sit amet consectetuer adipiscing elit sed diam nonummy nibh euismod.</p>
      <p>Quis nostrud exerci tation ullamcorper suscipit lobortis nisl ut aliquip ex ea commodo consequat. Ipsum dolor sit amet consectetuer adipiscing elit sed diam nonummy nibh.</p>
    </div>
    <div class="divider"></div>
    <div class="band">Et iusto odio dignissim qui blandit praesent</div>
    <ul class="bullets">
      <li>Quis nostrud exerci tation ullamcorper suscipit lobortis nisl ut aliquip ex ea commodo consequat.</li>
      <li>Ipsum dolor sit amet consectetuer adipiscing elit sed diam</li>
    </ul>
    <div class="divider"></div>
    <div class="band">Ut laoreet dolore magna, aliquam erat</div>
    <div class="story">
      <div class="photo" role="img" aria-label="Story photograph"></div>
      <p>Quis nostrud exerci tation ullamcorper suscipit lobortis nisl ut aliquip ex ea commodo consequat. Ipsum dolor sit amet consectetuer adipiscing elit sed diam nonummy nibh euismod tincidunt. Demonstraverunt lectores legere me lius quod ii legunt saepius claritas est etiam processus dynamicus qui sequitur. Quis nostrud exerci tation ullamcorper suscipit lobortis nisl ut aliquip ex ea commodo consequat. Ipsum dolor sit amet consectetuer adipiscing elit sed diam nonummy nibh euismod.</p>
      <p>Quis nostrud exerci tation ullamcorper suscipit lobortis nisl ut aliquip ex ea commodo consequat. Ipsum dolor sit amet consectetuer adipiscing elit sed diam nonummy nibh.</p>
    </div>
  </main>

  <footer class="site-footer">
    Northgate Filings LLC, 1290 West Alder St., Suite 310 Denver, CO 80204<br>
    Toll:<br>Phone:<br>Fax:<br>
    Don't want to receive these emails anymore? You can <a href="#">unsubscribe</a>
  </footer>
</div>
</body>
</html>
```